Pelham Design & Millwork needs a web presence. Looking for a unique Design so please submit an idea.

In brief, you should know the following about me: My company was established in 2001 and had been responsible for providing reasonable CAD Design and Custom Millwork ever since. My specialty is in the area Architectural CAD Design, Fabrication of Custom Millwork and Mouldings on a partime basis. Drawings and estimates done at a very reasonable cost. I look forward to working on your next project. Thanks in Advance, Boyd 
I would like one page to show thumbnails linked to some of past millwork projects and another page with thumbnails linking to some of my house designs. I assume last page will have contact information accessed from a link on home page. I already had a logo designed which I can supply you with to design home page around. As I indicated I have a regular full time job and do this for additional income and will move to full time when I have enough business.

I have attached the logo I had designed in a couple different colors. I have also uploaded some PDF's of files that I also considered before choosing the RED LOGO to give an ideas of how we could tweak the logo to better fit the website if need be. Text is wrong in those.

Thanks,
Boyd

I added my logo as a PDF side there seems to be a problem with scaling loge with the other file. Hope this helps.

Boyd

Evening,
I will be hosting this site on wavecrib. Its looks like it will get launched with wordpress?  What will be involved from getting your design up so I can upload project pictures and and text to areas you have set aside? I am also going to upload a couple jpg of a couple recent projects so you can put in so I can get a feel of what they will look like. Thanks for all your work to date! Boyd

I am not seeing alot of design variations or even many designers in fact. Is there something more from me you need? BP you need me to extend deadline?

Reason: It appears that your need some more time to submit some design changes. I will choose a design next week after changes have been submitted. Thanks for your time. Boyd

Reason: Designers needs a couple days to submit some last minute changes. Thanks for all your submissions! Boyd

Reason: Some last minute designs that I need to look at and give feedback on. I want to thank everyone for their designs and patience. Thanks again, Boyd

Evening All,

Upon discussion with a couple of the designers I want the design done in Word Press and I have increased budget the amount they said they would need to do it for. Thanks for all submissions so far but I am still looking for the special one that stands out among the rest! Boyd

I will not be extending deadline and choosing designer tomorrow morning so if you have anything else to add please do so tonight. Thanks for all your submissions. Boyd

Target Market(s)

Millwork projects will be generally local where as CAD Design Projects could be emailed anywhere. Probably more USA but who knows.

Industry/Entity Type

House

Font styles to use
Other font styles liked:
• Eras Medium ITC, Calibri or Designers choice.

Requirements
Must have
• Must tie in my logo on Homepage at least. Could even be somewhat transparent in background? I will let the designer work that out.
Nice to have
• Page to point to current and past Design projects on one page and millwork on another.
Should not have
• Target a large Corporate or Global environment since it is a small business right now.

```html
<!DOCTYPE html>
<html lang="en">
<head>
<meta charset="utf-8">
<title>Pelham Design &amp; Millwork</title>
<link rel="stylesheet" href="https://fonts.googleapis.com/css2?family=Exo:wght@400;700&family=Open+Sans:wght@400;600&family=Roboto:wght@400;700&display=swap">
<style>
:root{
  --red:#c41f25;
  --red-bright:#e8262b;
  --dark:#252628;
  --darker:#1b1b1c;
  --panel:rgba(20,20,20,.9);
  --light:#ececec;
  --white:#fff;
  --text:#444;
  --muted:#bfbfbf;
}
*{margin:0;padding:0;box-sizing:border-box}
html,body{width:880px;height:1200px;overflow:hidden;background:var(--light)}
.page{position:relative;width:880px;height:1200px;font-family:"Open Sans",sans-serif}
.hero{position:absolute;left:0;top:0;width:880px;height:474px;
  background:linear-gradient(160deg,#5f7fb8 0%,#a9c3e6 35%,#d8dde3 55%,#8b8f95 75%,#b9272b 100%)}
.site-nav{position:absolute;left:99px;top:23px;width:191px;height:345px;background:var(--panel)}
.brand{position:absolute;left:18px;top:34px;width:160px;display:flex;align-items:center;gap:7px;
  font-family:"Exo",sans-serif;font-weight:700;font-size:14px;line-height:1.2;color:var(--red-bright)}
.brand-mark{flex:none;width:16px;height:16px;background:var(--red-bright)}
.menu{position:absolute;left:8px;top:174px;width:179px;list-style:none}
.menu li{height:34px;border-bottom:1px solid #3a3a3a;padding-left:14px;
  font-family:"Exo",sans-serif;font-size:14px;letter-spacing:.6px;color:#cfcfcf;line-height:32px}
.menu li:last-child{border-bottom:none}
.menu li.active{color:var(--white);position:relative}
.menu li.active::before{content:"";position:absolute;left:-8px;top:7px;width:5px;height:18px;background:var(--red-bright)}
.services{position:absolute;left:0;top:474px;width:880px;height:287px;background:var(--red)}
.service{position:absolute;top:-49px;width:220px;text-align:center;color:var(--white)}
.service-photo{display:block;margin:0 auto;width:138px;height:138px;border-radius:50%;border:4px solid #f4f4f4;
  box-shadow:0 2px 6px rgba(0,0,0,.35)}
.service h2{font-family:"Exo",sans-serif;font-weight:700;font-size:16px;line-height:19px;margin-top:24px;letter-spacing:.3px}
.service p{font-size:9.6px;line-height:13px;margin:18px auto 0;width:172px;letter-spacing:.3px}
.btn{display:inline-block;margin-top:18px;width:88px;height:21px;line-height:19px;background:#1c1c1c;
  border:1px solid #666;color:var(--white);font-size:9.4px;letter-spacing:.5px}
.projects{position:absolute;left:0;top:761px;width:880px;height:262px}
.projects h3{position:absolute;font-family:"Exo",sans-serif;font-weight:400;font-size:17.5px;letter-spacing:.6px;color:#333}
.card{position:absolute;background:var(--white);border:1px solid #ddd;border-radius:3px;box-shadow:0 0 4px rgba(0,0,0,.06)}
.card::before{content:"";position:absolute;left:20px;top:-7px;width:12px;height:12px;background:var(--white);
  border-left:1px solid #ddd;border-top:1px solid #ddd;transform:rotate(45deg)}
.entry{position:absolute;left:10px;display:flex;gap:9px;font-family:"Roboto",sans-serif;font-size:8.4px;line-height:12.5px;color:var(--text)}
.thumb{flex:none;width:76px;height:42px}
.steps{list-style:none;position:absolute;left:10px;top:14px;font-family:"Roboto",sans-serif;font-size:9.4px;color:var(--text)}
.steps li{height:22.5px}
.steps span{color:var(--red-bright);margin-right:5px}
.footer{position:absolute;left:0;top:1023px;width:880px;height:150px;background:var(--dark);color:var(--white)}
.col{position:absolute;top:14px}
.col h4{font-family:"Roboto",sans-serif;font-weight:700;font-size:15.5px;padding-left:10px;height:30px}
.rule{height:4px;background:#4a4d52}
.col p{font-family:"Roboto",sans-serif;font-size:8.4px;line-height:16.6px;color:var(--muted);padding:14px 12px 0}
.social{display:flex;gap:5px;padding:6px 0 0 12px}
.social i{width:20px;height:20px;border-radius:2px;display:block}
.tags{display:flex;flex-wrap:wrap;gap:8px 6px;padding-top:14px}
.tags span{background:var(--red-bright);font-family:"Roboto",sans-serif;font-size:8.8px;padding:0 7px;height:23px;line-height:23px}
.copyright{position:absolute;left:0;top:1173px;width:880px;height:27px;background:var(--darker);
  color:#9a9a9a;font-family:"Roboto",sans-serif;font-size:9.6px;text-align:center;line-height:27px}
</style>
</head>
<body>
<div class="page">
  <div class="hero" role="img" aria-label="Photo of a modern building with a white lattice canopy and red facade against a blue sky"></div>

  <nav class="site-nav">
    <div class="brand"><span class="brand-mark"></span><span>Pelham Design &amp; Millwork</span></div>
    <ul class="menu">
      <li class="active">Home</li>
      <li>About BP</li>
      <li>Our Services</li>
      <li>Testimonials</li>
      <li>Contact Us</li>
    </ul>
  </nav>

  <section class="services">
    <div class="service" style="left:102px">
      <div class="service-photo" role="img" aria-label="Caliper and bearing resting on technical drawings" style="background:radial-gradient(circle,#d9d9d9,#9a9a9a)"></div>
      <h2>Architectural CAD<br>Design</h2>
      <p>I'm a paragraph. Click here to add your own text and edit me. Let your users get to know you simply dummy text of the printing</p>
      <span class="btn">Read More</span>
    </div>
    <div class="service" style="left:330px">
      <div class="service-photo" role="img" aria-label="Curved custom wooden millwork counter" style="background:radial-gradient(circle,#e0a45a,#7a4a1d)"></div>
      <h2 style="margin-top:20px">Fabrication of Custom<br>Millwork</h2>
      <p>I'm a paragraph. Click here to add your own text and edit me. Let your users get to know you simply dummy text of the printing</p>
      <span class="btn">Read More</span>
    </div>
    <div class="service" style="left:558px">
      <div class="service-photo" role="img" aria-label="3D floor plan of a house interior" style="background:radial-gradient(circle,#ebe6da,#a89f8d)"></div>
      <h2>Architectural<br>Mouldings</h2>
      <p>I'm a paragraph. Click here to add your own text and edit me. Let your users get to know you simply dummy text of the printing</p>
      <span class="btn">Read More</span>
    </div>
  </section>

  <section class="projects">
    <h3 style="left:98px;top:40px">Past Design projects</h3>
    <div class="card" style="left:92px;top:82px;width:309px;height:136px">
      <div class="entry" style="top:17px">
        <div class="thumb" role="img" aria-label="Construction site with cranes at dusk" style="background:linear-gradient(#8aa3c4,#6b5a44)"></div>
        <p>Lorem Ipsum has been the industry's standard<br>dummy text ever since the 1500s, when an<br>unknown printer</p>
      </div>
      <div class="entry" style="top:77px">
        <div class="thumb" role="img" aria-label="Wooden millwork counter project" style="background:linear-gradient(#c99a5b,#6e4420)"></div>
        <p>Lorem Ipsum has been the industry's standard<br>dummy text ever since the 1500s, when an<br>unknown printer</p>
      </div>
    </div>
    <h3 style="left:439px;top:43px">Millwork on another</h3>
    <div class="card" style="left:438px;top:80px;width:336px;height:135px">
      <ol class="steps">
        <li><span>1.</span>simply dummy text of the printing and typesetting</li>
        <li><span>2.</span>when an unknown took a printer took a galley of type and scrambled</li>
        <li><span>3.</span>It has survived not only five &nbsp;not centuries, but also into electronic</li>
        <li><span>4.</span>It was popularised in the &nbsp;not only 1960s with the of Letraset sheets</li>
        <li><span>5.</span>Lorem Ipsum passages, and &nbsp;not only more recently with desktop</li>
      </ol>
    </div>
  </section>

  <footer class="footer">
    <div class="col" style="left:90px;width:232px">
      <h4>How we differ/About</h4>
      <div class="rule"></div>
      <p>Sed luctus leo quis sapien tempor eu convallis tincidunt. Maecenas lorem nisi, dictum eget ornare a magna. Etiam volutpat consequat lorem nisi, dictum eget sollicitudin.</p>
    </div>
    <div class="col" style="left:351px;width:196px">
      <h4 style="padding-left:13px">Stay Connected</h4>
      <div class="rule"></div>
      <p style="padding-left:10px">Sed luctus leo quis sapien tempor eu convallis tincidunt. Maecenas lorem nisi, dictum eget...</p>
      <div class="social" style="padding-left:10px">
        <i style="background:#ea4c89"></i><i style="background:#5ba525"></i><i style="background:#3b5998"></i><i style="background:#f4f4f4"></i><i style="background:#8a6d57"></i><i style="background:#f39200"></i>
      </div>
    </div>
    <div class="col" style="left:584px;width:204px">
      <h4 style="padding-left:5px">Quick Links</h4>
      <div class="rule"></div>
      <div class="tags">
        <span>Business</span><span>Dating</span><span>Fashion</span><span>Movies</span><span>Photography</span><span>Technology</span>
      </div>
    </div>
  </footer>
  <div class="copyright">Copyright © 2014 Boyd Pelham. &nbsp;All Rights Reserved. &nbsp;Your Company Inc.</div>
</div>
</body>
</html>
```